Book cover for "HUMMING CROW and the BIG PARADE"

FROM THE SUBMISSIONS I DO NOT THINK MANY OF THE ARTISTS ARE SERIOUSLY READING MY BRIEF. "BAD ASS" MEANS AWSOME! WOW FACTOR.....NO REAL DOGS PLEASE...HUMMING CROW IS MY ALTER EGO...
R E A D THE B R I E F!! =(:0

I need a mind blowing cool creative cover for my book. It will be on "Print nook" on Fablet and in paperback.

This is my book full of true adventures of my life. If you meshed The Marlow Pardon with Rust and Rumbling in Old Tucumcari with The Neon Birch Candy Bus Ride then added a little Pears of Sorrow and added elements from the book "Hold My Kite... Then you would have an idea of content. If you are not familiar with any of these movies or books it is about survival, personal loss tragedy and the triumph of the human spirit. It is about life lessons and hope and humor and in the end, success.

I describe "Humming Crow" in the book as "A hip jive jungle cat who walks with a pimp limp" THINK "BIXBY O'FARREL" FROM THE OLD HOLLENTAP COMMERCIALS ... BULL TERRIER...He is a ladies man and smokes and drinks and stays out all night. Wears Cobalt blue sunglasses and lots of jewelry. He is mostly just "Cool like that".

HUMMING CROW...I got the name Humming Crow from a conversation where explained a mistake I had made at work - in anger I said to my Fleet manager "Well I guess I'm just stupid!" To which he replied, "I don't buy that because I have read your stories and I know your smart." I then told him "just because I have this one little bit of talent does not make me smart, like if you came home one day and found out your dog could talk. Yes, that would be AMAZING! But maybe the next day you back the car from the driveway and run over and kill him because he was lying in the sun licking his n%$&, he is a dog after all. So having one special talent does not mean your smart - and that is how humming crow was born. I have a talent, so they say but I could end up like the dog because I do really stupid stuff.

BIG PARADE....I got BIG PARADE from listening to an WBQ radio program.
The interviewer was talking to a lady who married a rich Iraqi student while they both were attending the same university. After university they moved to Iraq. Soon she found herself a virtual prisoner of her husband and Sharia law. Long story short after 5 years she escaped and returned to the United States and wrote a book about her experiences. She told the WBQ interviewer that "This experience provided her with a treasure chest of stories that allowed her to write the book." I said out loud to the radio, "Well if that was a treasure chest - then I have the ever loving BIG PARADE!"

What I'm looking for in COLORS are of course like everyone else...EYE
CATCHING...Bright...Bold...Oranges, Yellows, Turquoise Cobalt blue.. Book
covers by NED FALCONER comes to mind. I need original. Cool, hip tough guy
survivor... My stories appeal especially to women. Comments like, Dwayne, not only did I cry but I had tears streaming down my face or, I started reading it and couldn't stop...I get that a lot.

I'm open to FONT STYLES...I used IMPACT for my own creation. I made up a book cover a couple years ago (attached) just to make it seem more real to me. The vehicle that carries most all the stories is travelling....I went to 13 different schools growing up, I have hitchhiked more than 100,000 miles and for the last ten years I have been an over the road truck driver with more than one million miles of safe accident free driving. I grew up living in cars and vans on the road, so the American highway plays an important role in my life and carries my stories in the book.

I spent 7 years writing this, although we are only releasing a very small portion here in the beginning, this will be a 5 book series covering almost 60 years in the life of the most amazing adventures you have ever heard or read about.

I have put blood sweat and tears into this and agonized over every word. I am a high school drop out and twice convicted felon (27 YEARS AGO) and taught myself how to write. I never ask for anything from anyone and I have scratched and fought to get where I am today...the proverbial "Self made man".

In closing, I would be partial to a bold, humorous irreverent suave tough edgy risk taking design... I trust the artist to know their own work and put best fonts with their color scheme and design creation. I'm a traveling man, the cover does not have to have a Humming Crow in it with a graphic to represent the BIG PARADE but it can...I'm too close to this...I need a BRILLIANT design...The winning design will make me say "WOW!!"

I'm a trail blazer and hell raiser .... Rock - a Rolla... This book is a mind blowing rocking wild adventure with enough freaks to be its own circus...I don't know what else to say except I NEED A BAD ASS COVER DESIGN... Thank you....
P.S. THIS IS FOR A PAPERBACK BOOK, I BELIEVE THE DIMENSIONS WILL BE .. 8" H X 5" W

Target Market(s)

ALL PEOPLE, ALL WALKS OF LIFE

Industry/Entity Type

Book Publisher

Font styles to use
Serif
Sans Serif

Colors
0456a4
33a6d7
fbee3e
85cae6
000000
959595

Requirements
Must have
• HUMMING CROW and the BIG PARADE
• DWAYNE HOLLOWAY
Nice to have
• gradient shaded lettering
Should not have
• ANYTHING THAT MAKES IT LOOK LIKE A CHILDREN'S BOOK,

```html
<!DOCTYPE html>
<html lang="en">
<head>
<meta charset="utf-8">
<title>Humming Crow and the Big Parade — Book Cover</title>
<link rel="stylesheet" href="https://fonts.googleapis.com/css2?family=Oswald:wght@600&family=Baloo+2:wght@800&family=Ribeye&family=Architects+Daughter&display=swap">
<style>
  :root {
    --night: #0e0c08;
    --haze: #6b5f45;
    --haze-soft: #3a3326;
    --title-yellow: #ffff1f;
    --white: #ffffff;
    --band-teal: #13d6d4;
    --shadow: rgba(0, 0, 0, 0.85);
  }
  html, body {
    margin: 0;
    padding: 0;
    width: 1200px;
    height: 1000px;
    overflow: hidden;
    background: var(--night);
  }
  .cover {
    position: relative;
    width: 1200px;
    height: 1000px;
    overflow: hidden;
  }
  .cover-scene {
    position: absolute;
    inset: 0;
    background:
      radial-gradient(ellipse 520px 300px at 260px 140px, rgba(120,108,78,0.55), transparent 70%),
      linear-gradient(155deg, var(--haze-soft) 0%, var(--haze) 30%, #4a412f 48%, #1c1810 70%, var(--night) 100%);
  }
  .title {
    position: absolute;
    left: 0;
    width: 100%;
    margin: 0;
    text-align: center;
    text-shadow: 6px 6px 6px var(--shadow);
  }
  .title-main {
    top: 128px;
    left: 10px;
    font-family: "Oswald", sans-serif;
    font-weight: 600;
    font-size: 150px;
    line-height: 1;
    letter-spacing: 4px;
    color: var(--title-yellow);
    transform: scaleY(1.15);
  }
  .title-joiner {
    top: 360px;
    font-family: "Baloo 2", sans-serif;
    font-weight: 800;
    font-style: italic;
    font-size: 100px;
    line-height: 1;
    letter-spacing: 6px;
    color: var(--white);
  }
  .title-sub {
    top: 505px;
    left: 4px;
    font-family: "Ribeye", serif;
    font-size: 132px;
    line-height: 1;
    letter-spacing: 2px;
    color: var(--title-yellow);
  }
  .author-band {
    position: absolute;
    left: 25px;
    top: 800px;
    width: 1146px;
    height: 136px;
    background: var(--band-teal);
    display: flex;
    align-items: center;
    justify-content: center;
  }
  .author-name {
    margin: 0;
    font-family: "Architects Daughter", cursive;
    font-size: 92px;
    line-height: 1;
    letter-spacing: 6px;
    color: var(--white);
    transform: skewX(-6deg);
  }
</style>
</head>
<body>
  <main class="cover">
    <div class="cover-scene" role="img" aria-label="Night scene of a dark farmhouse roof and wooden fence with a bare tree, a beam of hazy light cutting through the mist"></div>
    <h1 class="title title-main">HUMMING CROW</h1>
    <p class="title title-joiner">and the</p>
    <p class="title title-sub">BIG PARADE</p>
    <div class="author-band">
      <p class="author-name">DWAYNE HOLLOWAY</p>
    </div>
  </main>
</body>
</html>
```